vQTA Company brochure For sales and Marketing

WE need a brochure design for our company called vQTA. The logo is gold. This is an Airline Maintenace Software Company. The software it is called vQTA.

We will like the Brochure to include our modules and a brief description on what they are about.

The front cover we want to have purple night sky screen. With our logo and out motto.

The first page can have the company bio. And the inside the Company modules description.

the back can have contact Sales information.

We will like this to be modern and with style. Ower mention Perlotti catalog.

please see out sample Web Site

http://kdaran52.sitepadhub.com/vqta

Target Market(s)

Airlines

Industry/Entity Type

Airline

Requirements
Must have
• gold, black , purple, grey and chrome. we like mature scenes or night sky
Nice to have

```html
<!DOCTYPE html>
<html lang="en">
<head>
<meta charset="utf-8">
<title>vQTA Brochure Spread</title>
<link rel="stylesheet" href="https://fonts.googleapis.com/css2?family=Josefin+Sans:wght@300&family=Marcellus&display=swap">
<style>
  :root {
    --backdrop: #cdb08c;
    --paper: #ffffff;
    --gold: #c2a27a;
    --gold-light: #f1e3b8;
    --gold-deep: #b08d5e;
    --ink: #2e2a26;
    --tab: #1f1d1b;
    --sky-top: #c9ccd0;
    --sky-bottom: #6f7a66;
    --ui-blue: #2f6fc4;
    --ui-light: #eef1f5;
  }
  * { margin: 0; padding: 0; box-sizing: border-box; }
  html, body { width: 1200px; height: 1200px; overflow: hidden; }
  body { background: var(--backdrop); position: relative; font-family: "Marcellus", Georgia, serif; color: var(--ink); }

  .page {
    position: absolute; top: 270px; width: 510px; height: 660px;
    background: var(--paper); box-shadow: 0 2px 8px rgba(0,0,0,.25);
  }
  .page--bio { left: 56px; }
  .page--modules { left: 634px; }

  .bio__band { position: absolute; left: 191px; top: 0; width: 128px; height: 30px; background: var(--gold); }
  .bio__photo {
    position: absolute; left: 191px; top: 30px; width: 128px; height: 282px;
    background: linear-gradient(180deg, var(--sky-top) 0%, #e4e6e8 45%, #a9aeb0 75%, var(--sky-bottom) 100%);
  }
  .bio__logo {
    position: absolute; left: 0; width: 510px; top: 330px; text-align: center;
    font-size: 54px; line-height: 54px; color: var(--gold); letter-spacing: 1px;
  }
  .bio__text {
    position: absolute; left: 142px; top: 404px; width: 226px;
    font-size: 7.4px; line-height: 9.75px; text-align: justify; letter-spacing: .25px;
  }

  .module { position: absolute; left: 34px; width: 442px; height: 120px; }
  .module__screen {
    position: absolute; left: 0; top: 0; width: 139px; height: 116px;
    background: linear-gradient(180deg, var(--ui-blue) 0%, var(--ui-blue) 10%, var(--ui-light) 11%, #ffffff 60%, #e3e7ec 100%);
    box-shadow: 0 1px 3px rgba(0,0,0,.3);
  }
  .module__body { position: absolute; left: 172px; top: 0; width: 274px; }
  .module__title {
    font-family: "Josefin Sans", Arial, sans-serif; font-weight: 300;
    font-size: 12px; line-height: 13px; color: var(--gold); text-transform: uppercase;
    border-bottom: 0.8px solid var(--gold); padding-bottom: 0; letter-spacing: .2px;
  }
  .module__text {
    margin-top: 10px; font-size: 6.6px; line-height: 9.75px; text-align: justify; letter-spacing: .2px;
  }

  .footer-band {
    position: absolute; left: 0; top: 630px; width: 510px; height: 30px;
    background: linear-gradient(90deg, var(--gold-deep) 0%, var(--gold-light) 45%, var(--gold) 80%, var(--gold-deep) 100%);
  }
  .footer-band__tab { position: absolute; right: 0; top: 0; width: 66px; height: 30px; }
  .footer-band__num {
    position: absolute; right: 22px; top: 5px; color: #ffffff;
    font-family: "Josefin Sans", Arial, sans-serif; font-weight: 300; font-size: 18px;
  }
</style>
</head>
<body>

<section class="page page--bio">
  <div class="bio__band"></div>
  <div class="bio__photo" role="img" aria-label="Photo of an airliner nose and engine seen from below against a cloudy sky"></div>
  <div class="bio__logo">vQTA</div>
  <p class="bio__text">AVORA is well known within the aviation maintenance community as the bestselling MRO software on the market. AVORA is a comprehensive MRO ERP software designed to cater to virtually every aspect of aircraft maintenance. The AVORA Maintenance and Engineering solution has been developed with our users to provide the most comprehensive and advanced maintenance software solution available today, with the most impressive sales and implementation record of any MRO ERP software provider ever. AVORA continues to be committed to providing the finest software solution and services to its airline and MRO customers around the world. AVORA Maintenance is a fully integrated product which allows complete information flow between the modules in the system. The software provides the means to manage and maintain all information generated by a maintenance organization. Hardware and operating systems can be chosen to meet your specific requirements. Utilizing the latest Web technology, the AVORA application can also be entirely accessible via the internet. A native Panelo interface provides your users with a simple and easy to operate application. In addition, the AVORA mobile solution (AvoraM) gives you customized access to the most needed Avora capabilities when you're on the go such as mobility, real-time functionality, modern usability and security.</p>
</section>

<section class="page page--modules">
  <article class="module" style="top:32px">
    <div class="module__screen" role="img" aria-label="Screenshot of the requisition dashboard with pie charts and a bar chart"></div>
    <div class="module__body">
      <h2 class="module__title">The Requisition Module</h2>
      <p class="module__text">Real time creation of requisitions allows complete monitoring of all company part requirements. Requisitions automatically generate Inventory Transactions as defined by predetermined reorder level requirements. Requisition information can be tied to orders and updates upon satisfaction of such requirements. The electronic quoting system provides a way to send and receive quotes via email or Spec2000 transactions.</p>
    </div>
  </article>

  <article class="module" style="top:182px">
    <div class="module__screen" role="img" aria-label="Screenshot of the orders module form screen"></div>
    <div class="module__body">
      <h2 class="module__title">The Orders Modules</h2>
      <p class="module__text">The Orders module empowers you to create and monitor the following types of orders: Contract Order, Exchange In/Out Order, Loan Order, Purchase Order, Service Order, Repair Order, Customer Order, Rental Order, Manufacturer Order, Warranty Claim Order, Transfer Order and Insurance Claim. Receiving and Inspecting can be performed as required. Online vendor performance is graphically monitored. Electronic Ordering via Spec2000 is available as standard. Various connections to industry purchasing portals are also supported.</p>
    </div>
  </article>

  <article class="module" style="top:332px">
    <div class="module__screen" role="img" aria-label="Screenshot of the inventory module screen"></div>
    <div class="module__body">
      <h2 class="module__title">The Inventory Module</h2>
      <p class="module__text">This functionality gives you the ability to control inventory within your organization from the basic part requirement through to warehousing, reserving and issuing of parts such as serialized, non-serialized and kits. Multiple locations can be optimized for minimum inventory, thus reducing cost. You can also track the Packing and Shipping of parts with this module. Rotable and Consumable inventory optimization functions provide detailed analysis of part movements within the company and give recommendations on buying new stock or selling surplus stock according to the operational requirements. Bar coding and RFID are supported for tracking of materials through your organization.</p>
    </div>
  </article>

  <article class="module" style="top:482px">
    <div class="module__screen" role="img" aria-label="Screenshot of the financial interface module screen"></div>
    <div class="module__body">
      <h2 class="module__title">The Financial Interface Module</h2>
      <p class="module__text">The Finance module provides an interface with companies' financial software (such as General Ledger, Accounts Payable, and Receivable systems) to feed them information. The system keeps tight and accurate control over all financial information and produces journal entries for all financially related activity within the system. The fixed asset menu option provides valuation and depreciation data. Monthly balances, stock valuations, and financial budgeting are all accessible within the system.</p>
    </div>
  </article>

  <div class="footer-band">
    <svg class="footer-band__tab" viewBox="0 0 66 30" aria-hidden="true"><polygon points="0,0 66,0 66,30 14,30" fill="var(--tab)"/></svg>
    <span class="footer-band__num">3</span>
  </div>
</section>

</body>
</html>
```